Cloud Based Internet Protection Service Business Cards

I would like a professionally designed business card. I already have a logo which I have attached.

The business is an online cloud based internet protection service aimed parents, particularly at non-technical parents and also schools.

The card should be be quite simple in its design, not to full of text and give its information in a clear and concise manner

Target Market(s)

Parents (especially non-technical parents) and also schools

Industry/Entity Type

Internet

Colors

Designer to choose colors to be used in the design.

Requirements
Should not have
• Too much text or be too cluttered. No decorative fonts, just a clear and concise font.

```html
<!DOCTYPE html>
<html lang="en">
<head>
<meta charset="utf-8">
<title>Brightwall Business Cards</title>
<link href="https://fonts.googleapis.com/css2?family=Open+Sans:wght@400;600;700&display=swap" rel="stylesheet">
<style>
  :root {
    --backdrop: #e4e5e7;
    --card: #ffffff;
    --card-back: #f4f4f3;
    --navy: #0f3d5c;
    --blue: #2f7fc1;
    --ink: #1d2b36;
    --muted: #4a5560;
  }
  * { margin: 0; padding: 0; box-sizing: border-box; }
  html, body {
    width: 1200px; height: 675px; overflow: hidden;
    background: var(--backdrop);
    font-family: "Open Sans", Arial, sans-serif;
    color: var(--ink);
  }
  .stage {
    position: relative; width: 1200px; height: 675px;
    display: flex; align-items: center; justify-content: center; gap: 50px;
  }
  .card {
    position: relative; width: 525px; height: 300px;
    background: var(--card); overflow: hidden;
    box-shadow: 0 6px 18px rgba(0,0,0,0.12);
  }
  .card--back { background: var(--card-back); }
  .card__bands { position: absolute; left: 0; bottom: 0; width: 525px; height: 40px; }
  .band-navy { fill: var(--navy); }
  .band-blue { fill: var(--blue); }

  .brand { display: flex; align-items: center; gap: 10px; }
  .brand__dot { width: 16px; height: 16px; border-radius: 50%; background: var(--blue); }
  .brand__name { font-weight: 700; color: var(--navy); letter-spacing: 0.5px; }

  .card--front .brand { position: absolute; left: 0; right: 0; top: 112px; justify-content: center; }
  .card--front .brand__name { font-size: 40px; }

  .card--back .brand { position: absolute; left: 60px; top: 80px; }
  .card--back .brand__name { font-size: 30px; }

  .person { position: absolute; left: 150px; top: 200px; text-align: right; }
  .person__name { font-size: 15px; font-weight: 700; color: var(--navy); }
  .person__title { font-size: 11px; color: var(--muted); }

  .contact { position: absolute; left: 330px; top: 142px; list-style: none; }
  .contact__item { display: flex; align-items: center; gap: 7px; font-size: 11px; line-height: 17px; color: var(--ink); }
  .contact__icon { width: 10px; height: 10px; fill: var(--navy); flex: none; }
</style>
</head>
<body>
<main class="stage">
  <section class="card card--front" aria-label="Card front">
    <div class="brand">
      <span class="brand__dot"></span>
      <span class="brand__name">Brightwall</span>
    </div>
    <svg class="card__bands" viewBox="0 0 525 40" aria-hidden="true">
      <polygon class="band-navy" points="0,22 300,22 322,10 525,10 525,15 326,15 304,31 0,31"/>
      <polygon class="band-blue" points="322,10 525,10 525,4 334,4"/>
    </svg>
  </section>

  <section class="card card--back" aria-label="Card back">
    <div class="brand">
      <span class="brand__dot"></span>
      <span class="brand__name">Brightwall</span>
    </div>

    <div class="person">
      <p class="person__name">Your Long Name</p>
      <p class="person__title">Your Title</p>
    </div>

    <ul class="contact">
      <li class="contact__item">
        <svg class="contact__icon" viewBox="0 0 10 10"><path d="M5 0a3.5 3.5 0 0 1 3.5 3.5C8.5 6 5 10 5 10S1.5 6 1.5 3.5A3.5 3.5 0 0 1 5 0zm0 2a1.5 1.5 0 1 0 0 3a1.5 1.5 0 0 0 0-3z"/></svg>
        Your office or home address
      </li>
      <li class="contact__item">
        <svg class="contact__icon" viewBox="0 0 10 10"><path d="M2 0l2 2.5-1 1.2a6 6 0 0 0 3.3 3.3l1.2-1L10 8 8.5 10C4 9.5.5 6 0 1.5z"/></svg>
        000-000-0000 &nbsp;&middot;&nbsp; 0000000000
      </li>
      <li class="contact__item">
        <svg class="contact__icon" viewBox="0 0 10 10"><path d="M0 2h10v6H0z M0 2l5 3.5L10 2" fill="none" stroke="#0f3d5c" stroke-width="1.2"/></svg>
        yourname@yourwebsite.com
      </li>
      <li class="contact__item">
        <svg class="contact__icon" viewBox="0 0 10 10"><circle cx="5" cy="5" r="4.3" fill="none" stroke="#0f3d5c" stroke-width="1.1"/><path d="M0.7 5h8.6M5 0.7c-2.4 2.6-2.4 6 0 8.6M5 0.7c2.4 2.6 2.4 6 0 8.6" fill="none" stroke="#0f3d5c" stroke-width="0.9"/></svg>
        www.yourwebsite.com
      </li>
    </ul>

    <svg class="card__bands" viewBox="0 0 525 40" aria-hidden="true">
      <polygon class="band-navy" points="0,26 300,26 322,14 525,14 525,19 326,19 304,35 0,35"/>
      <polygon class="band-blue" points="322,14 525,14 525,8 334,8"/>
    </svg>
  </section>
</main>
</body>
</html>
```